Celebratory PNG Overlays for use on social media related to cryptocurrency project

We need a couple of Overlays to be used in social media sharing for people who achieve certain ranks among our team members.
Must Include our logo, the title DVK GALLANTS Beacons, congratulations and the different KRV Winnings (5 KRV, 50ETH, 500ETH and 1000ETH).
(we award physical coins to members who attain these ranks, example images are added, you can use these as inspiration but it is NOT mandatory only optional)
Please use the provided template in regards to the space were photo and name must go, similar example in use provided

Please check the files added

Font styles to use
Sans Serif
Decorative

Requirements
Must have
• Our logo, DVK Gallants Beacons , Congratulations and the different ammounts.
Must have the 2 items on the template.
Nice to have
• we award physical coins to members who attain these ranks, example images are added, you can use these as inspiration but it is NOT mandatory only optional)

```html
<!DOCTYPE html>
<html lang="en">
<head>
<meta charset="utf-8">
<title>DVK Gallants Beacons – 5 KRV Winner Overlay</title>
<link rel="stylesheet" href="https://fonts.googleapis.com/css2?family=Audiowide&family=Exo+2:ital,wght@1,800&display=swap">
<style>
  :root {
    --bg-deep: #2f2a4a;
    --bg-mid: #4a3f78;
    --bg-violet: #6a3fd0;
    --bg-magenta: #a43ccc;
    --gold-light: #fff27a;
    --gold: #f2c230;
    --gold-deep: #f08a12;
    --ring-shade: #b8a96a;
    --title-white: #ffffff;
    --title-orange: #f0872a;
    --photo-white: #ffffff;
    --name-panel: #e9e9e9;
    --name-strip: #c4747a;
    --band-dark: #232124;
    --band-edge: #c88a4a;
    --prize-pink: #e020b4;
    --prize-cyan: #19c9d8;
    --text-white: #ffffff;
    --coin-ghost: rgba(255, 255, 255, 0.14);
  }
  * { margin: 0; padding: 0; box-sizing: border-box; }
  html, body {
    width: 1127px;
    height: 1200px;
    overflow: hidden;
    background: var(--bg-deep);
  }
  .overlay {
    position: relative;
    width: 1127px;
    height: 1200px;
    overflow: hidden;
  }
  .overlay svg { position: absolute; inset: 0; display: block; }
  .title-text { font-family: "Audiowide", sans-serif; font-size: 92px; }
  .congrats-text { font-family: "Audiowide", sans-serif; font-size: 64px; fill: var(--text-white); }
  .prize-amount { font-family: "Exo 2", sans-serif; font-style: italic; font-weight: 800; fill: var(--prize-cyan); }
  .brand-name { font-family: "Audiowide", sans-serif; font-size: 62px; fill: var(--gold); }
</style>
</head>
<body>
<main class="overlay">
  <svg width="1127" height="1200" viewBox="0 0 1127 1200" xmlns="http://www.w3.org/2000/svg">
    <defs>
      <radialGradient id="backdropGradient" cx="45%" cy="40%" r="80%">
        <stop offset="0" stop-color="var(--bg-mid)"/>
        <stop offset="0.55" stop-color="var(--bg-violet)"/>
        <stop offset="1" stop-color="var(--bg-magenta)"/>
      </radialGradient>
      <linearGradient id="titleGradient" x1="0" y1="0" x2="1" y2="0">
        <stop offset="0" stop-color="var(--title-white)"/>
        <stop offset="0.45" stop-color="#f7c46a"/>
        <stop offset="1" stop-color="var(--title-orange)"/>
      </linearGradient>
      <linearGradient id="ringGradient" x1="0" y1="0" x2="1" y2="1">
        <stop offset="0" stop-color="var(--gold-deep)"/>
        <stop offset="0.35" stop-color="var(--gold-light)"/>
        <stop offset="0.7" stop-color="var(--gold)"/>
        <stop offset="1" stop-color="var(--gold-deep)"/>
      </linearGradient>
      <radialGradient id="coinGradient" cx="40%" cy="35%" r="70%">
        <stop offset="0" stop-color="#fff4b8"/>
        <stop offset="0.6" stop-color="var(--gold)"/>
        <stop offset="1" stop-color="var(--gold-deep)"/>
      </radialGradient>
      <filter id="softShadow" x="-20%" y="-20%" width="140%" height="140%">
        <feDropShadow dx="0" dy="8" stdDeviation="10" flood-color="#000" flood-opacity="0.45"/>
      </filter>
    </defs>

    <rect class="backdrop" role="img" aria-label="Violet and purple diamond pattern background"
          width="1127" height="1200" fill="url(#backdropGradient)"/>

    <g class="ghost-coins">
      <circle cx="124" cy="321" r="60" fill="var(--coin-ghost)" stroke="rgba(255,255,255,0.25)" stroke-width="5"/>
      <circle cx="976" cy="451" r="60" fill="var(--coin-ghost)" stroke="rgba(255,255,255,0.25)" stroke-width="5"/>
    </g>

    <text class="title-text" x="21" y="137" fill="url(#titleGradient)"
          textLength="1085" lengthAdjust="spacingAndGlyphs">DVK GALLANTS BEACONS</text>

    <g class="photo-frame" filter="url(#softShadow)">
      <circle cx="553" cy="421" r="274" fill="url(#ringGradient)"/>
      <circle cx="565" cy="423" r="258" fill="var(--ring-shade)"/>
      <circle class="photo-slot" cx="558" cy="418" r="246" fill="var(--photo-white)"/>
    </g>

    <g class="name-plate">
      <polygon points="204,700 990,641 990,706 204,706" fill="var(--name-strip)"/>
      <polygon points="131,714 916,651 916,814 131,814" fill="var(--name-panel)" filter="url(#softShadow)"/>
    </g>

    <text class="congrats-text" x="25" y="904" textLength="736" lengthAdjust="spacingAndGlyphs">CONGRATULATIONS</text>
    <text class="congrats-text" x="289" y="966" textLength="352" lengthAdjust="spacingAndGlyphs">YOU WON</text>

    <path class="bottom-band" d="M0,1071 Q330,990 760,1000 L1127,1040 L1127,1200 L0,1200 Z" fill="var(--band-dark)"/>
    <path d="M0,1071 Q330,990 760,1000" fill="none" stroke="var(--band-edge)" stroke-width="6"/>

    <g class="prize-badge">
      <polygon points="609,993 862,866 1113,998 873,1141" fill="var(--prize-pink)"/>
      <text class="prize-amount" x="824" y="1058" font-size="140" text-anchor="middle">5</text>
      <text class="prize-amount" x="945" y="1036" font-size="46" text-anchor="middle">KRV</text>
    </g>

    <g class="award-coin" filter="url(#softShadow)">
      <circle cx="988" cy="817" r="126" fill="#fff6d0"/>
      <circle cx="988" cy="817" r="112" fill="url(#coinGradient)"/>
    </g>

    <g class="brand-mark">
      <circle cx="158" cy="1123" r="55" fill="var(--gold)"/>
      <text class="brand-name" x="240" y="1155" textLength="493" lengthAdjust="spacingAndGlyphs">DVK GALLANTS</text>
    </g>
  </svg>
</main>
</body>
</html>
```